Business Card Design Project

We are an incubator company that helps young entrepreneur to launch new ideas into the market. We will be targeting investors or likewise; Angels, young entrepreneurs and technopreneurs.

Our logo is being tasked by artflockly to design, therefore there is no logo for now.
You can us Lanternfold Pte Ltd as the logo for the time being.

Please let us have some versions of modern and yet professional designs; for words, you can indicate e.g (address), (Title)

thanks

Target Market(s)

young entrepreneurs
angels, investors

Industry/Entity Type

Business

Colors
3176b5
ffffff

Requirements
Must have
• able to project out our name; Lanternfold
Should not have
• Nothing childish or cartoon

```html
<!DOCTYPE html>
<html lang="en">
<head>
<meta charset="utf-8">
<title>Lanternfold Business Card</title>
<link rel="stylesheet" href="https://fonts.googleapis.com/css2?family=Roboto+Condensed:wght@400;700&family=Open+Sans:wght@400;700&display=swap">
<style>
  :root {
    --brand-blue: #1f5fa8;
    --brand-blue-deep: #0e4a94;
    --band-grey: #7a7a7a;
    --ink: #2b2b2b;
    --card: #ffffff;
    --backdrop: #ececec;
  }
  * { margin: 0; padding: 0; box-sizing: border-box; }
  html, body {
    width: 1200px; height: 1001px; overflow: hidden;
    background: var(--backdrop);
  }
  .sheet { position: relative; width: 1200px; height: 1001px; }
  .card {
    position: absolute; top: 346px;
    width: 540px; height: 309px;
    background: var(--card);
    box-shadow: 0 6px 18px rgba(0,0,0,0.12);
    overflow: hidden;
  }
  .card--contact { left: 40px; }
  .card--brand { left: 620px; }

  .band { position: absolute; height: 7px; top: 200px; }
  .band--blue { background: var(--brand-blue-deep); }
  .band--grey { background: var(--band-grey); }

  .holder-name {
    position: absolute; left: 40px; top: 32px;
    font-family: "Open Sans", sans-serif; font-weight: 700;
    font-size: 17px; color: var(--brand-blue);
  }
  .holder-title {
    position: absolute; left: 40px; top: 57px;
    font-family: "Open Sans", sans-serif; font-size: 11px; color: var(--ink);
  }
  .contact-list {
    position: absolute; left: 40px; top: 94px;
    font-family: "Roboto Condensed", sans-serif; font-size: 13px;
    color: var(--ink); line-height: 18px; list-style: none;
  }
  .contact-item { display: flex; gap: 8px; }
  .contact-icon { flex: none; width: 12px; margin-top: 3px; display: flex; justify-content: center; }

  .wordmark { position: absolute; display: flex; align-items: center; gap: 10px; }
  .wordmark-square {
    width: 26px; height: 26px; background: var(--brand-blue-deep); border-radius: 3px;
  }
  .wordmark-text { display: flex; flex-direction: column; }
  .wordmark-name {
    font-family: "Open Sans", sans-serif; font-weight: 700;
    font-size: 28px; letter-spacing: 1px; line-height: 1;
    color: var(--brand-blue-deep); text-transform: uppercase;
  }
  .wordmark-tagline {
    font-family: "Open Sans", sans-serif; font-size: 8.5px;
    letter-spacing: 3.4px; color: var(--band-grey);
    text-transform: uppercase; margin-top: 4px;
  }
  .card--contact .wordmark { right: 30px; bottom: 34px; }
  .card--brand .wordmark { left: 130px; top: 120px; }
</style>
</head>
<body>
<main class="sheet">

  <section class="card card--contact" aria-label="Card back with contact details">
    <p class="holder-name">Daniel Koh</p>
    <p class="holder-title">Director</p>
    <ul class="contact-list">
      <li class="contact-item">
        <span class="contact-icon">
          <svg width="10" height="13" viewBox="0 0 10 13" aria-hidden="true">
            <path d="M5 0a5 5 0 0 1 5 5c0 3.5-5 8-5 8S0 8.5 0 5a5 5 0 0 1 5-5z" fill="var(--brand-blue)"/>
            <circle cx="5" cy="5" r="1.8" fill="#fff"/>
          </svg>
        </span>
        <span>12 Harbour Row<br>Cedarline Building<br>#04-02<br>Singapore 318920</span>
      </li>
      <li class="contact-item">
        <span class="contact-icon">
          <svg width="12" height="12" viewBox="0 0 12 12" aria-hidden="true">
            <path d="M2.5 0.5l2 2.5-1.2 1.4a7 7 0 0 0 4.3 4.3L9 7.5l2.5 2-1.5 2C5 11.5 0.5 7 0.5 2z" fill="var(--brand-blue)"/>
          </svg>
        </span>
        <span>+65 8123 4567</span>
      </li>
    </ul>
    <div class="band band--blue" style="left:0; width:300px;"></div>
    <div class="band band--grey" style="left:300px; width:60px;"></div>
    <div class="wordmark">
      <span class="wordmark-square" aria-hidden="true"></span>
      <div class="wordmark-text">
        <span class="wordmark-name">Lanternfold</span>
        <span class="wordmark-tagline">Launching Bold Ventures</span>
      </div>
    </div>
  </section>

  <section class="card card--brand" aria-label="Card front with company name">
    <div class="wordmark">
      <span class="wordmark-square" aria-hidden="true"></span>
      <div class="wordmark-text">
        <span class="wordmark-name">Lanternfold</span>
        <span class="wordmark-tagline">Launching Bold Ventures</span>
      </div>
    </div>
    <div class="band band--grey" style="left:0; width:120px;"></div>
    <div class="band band--blue" style="left:120px; width:420px;"></div>
  </section>

</main>
</body>
</html>
```